Brightwire Hollow Business cards

one side I would like my logo (uploaded) and the other side I want my details. I'm an electrician in sydney. The logo side I'm happy with just a white background and our logo in the middle.

Details for other side
24/7 Sydney Electrician
Marcus Pell
0431 587 219
marcus@brightwirehollow.com.au
brightwirehollow.com.au
icons for facebook, instagram, linked in

Industry/Entity Type

electrician

Contact Information for Business Card

company info

```html
<!DOCTYPE html>
<html lang="en">
<head>
<meta charset="utf-8">
<title>Brightwire Hollow Business Cards</title>
<link href="https://fonts.googleapis.com/css2?family=Open+Sans:ital,wght@0,400;0,600;0,700;0,800;1,600;1,800&display=swap" rel="stylesheet">
<style>
  :root {
    --backdrop: #808080;
    --card: #ffffff;
    --brand-red: #ee3524;
    --ink: #111111;
    --muted: #6b6b6b;
    --divider: #cfcfcf;
    --band: #000000;
    --band-text: #8c8c8c;
  }
  * { margin: 0; padding: 0; box-sizing: border-box; }
  html, body {
    width: 1200px; height: 1000px; overflow: hidden;
    background: var(--backdrop);
    font-family: "Open Sans", Arial, sans-serif;
  }
  .stage { position: relative; width: 1200px; height: 1000px; }
  .card {
    position: absolute;
    width: 613px; height: 352px;
    background: var(--card);
    border-radius: 26px;
    overflow: hidden;
    box-shadow: 0 20px 40px rgba(0,0,0,0.35);
  }
  .card--front { left: 293px; top: 123px; }
  .card--back { left: 294px; top: 520px; }

  .wordmark {
    color: var(--brand-red);
    font-weight: 800;
    text-transform: uppercase;
    line-height: 1.05;
    letter-spacing: 0.04em;
  }
  .card--front .wordmark {
    position: absolute; left: 0; right: 0; top: 252px;
    text-align: center; font-size: 36px;
  }
  .social {
    position: absolute; left: 0; right: 0; top: 302px;
    display: flex; justify-content: center; gap: 10px;
  }
  .social__dot {
    width: 20px; height: 20px; border-radius: 50%;
    background: var(--brand-red);
  }

  .identity {
    position: absolute; left: 0; top: 117px;
    width: 306px; height: 97px;
    display: flex; align-items: center; justify-content: center;
  }
  .card--back .wordmark { font-size: 25px; text-align: center; }
  .divider {
    position: absolute; left: 306px; top: 117px;
    width: 1px; height: 97px; background: var(--divider);
  }
  .details { position: absolute; left: 331px; top: 114px; }
  .details__name {
    font-size: 20px; font-weight: 600; color: var(--ink);
    margin-bottom: 13px;
  }
  .details__line {
    display: flex; align-items: center; gap: 8px;
    font-size: 15px; color: var(--muted); height: 20px;
  }
  .details__line svg { width: 14px; height: 14px; fill: var(--brand-red); flex: none; }

  .tagline-band {
    position: absolute; left: 0; bottom: 0;
    width: 100%; height: 56px; background: var(--band);
    display: flex; align-items: center; justify-content: center;
    font-style: italic; font-size: 15px; text-transform: uppercase;
  }
  .tagline-band svg { width: 10px; height: 18px; fill: var(--brand-red); margin-right: 1px; }
  .tagline-band__hours { color: var(--brand-red); font-weight: 800; font-size: 19px; margin-right: 4px; }
  .tagline-band__trade { color: var(--band-text); font-weight: 600; }
</style>
</head>
<body>
<main class="stage">
  <section class="card card--front" aria-label="Card front">
    <div class="wordmark">Brightwire Hollow</div>
    <div class="social" aria-label="Social links">
      <span class="social__dot"></span>
      <span class="social__dot"></span>
      <span class="social__dot"></span>
    </div>
  </section>

  <section class="card card--back" aria-label="Card back">
    <div class="identity"><div class="wordmark">Brightwire<br>Hollow</div></div>
    <div class="divider"></div>
    <div class="details">
      <div class="details__name">Marcus Pell</div>
      <div class="details__line">
        <svg viewBox="0 0 24 24"><path d="M6.6 10.8a15.1 15.1 0 0 0 6.6 6.6l2.2-2.2c.3-.3.7-.4 1-.2 1.1.4 2.3.6 3.6.6.6 0 1 .4 1 1V20c0 .6-.4 1-1 1A17 17 0 0 1 3 4c0-.6.4-1 1-1h3.5c.6 0 1 .4 1 1 0 1.3.2 2.5.6 3.6.1.3 0 .7-.2 1z"/></svg>
        <span>0431 587 219</span>
      </div>
      <div class="details__line">
        <svg viewBox="0 0 24 24"><path d="M2 5h20v3l-10 6L2 8z"/><path d="M2 10l10 6 10-6v9H2z"/></svg>
        <span>marcus@brightwirehollow.com.au</span>
      </div>
      <div class="details__line">
        <svg viewBox="0 0 24 24"><path d="M12 2a10 10 0 1 0 0 20 10 10 0 0 0 0-20zm6.9 6h-2.9a15 15 0 0 0-1.4-3.6A8 8 0 0 1 18.9 8zM12 4c.8 1.2 1.5 2.5 1.9 4h-3.8c.4-1.5 1.1-2.8 1.9-4zM4.3 14a8 8 0 0 1 0-4h3.3a16 16 0 0 0 0 4zm.8 2h2.9c.3 1.3.8 2.5 1.4 3.6A8 8 0 0 1 5.1 16zM8 8H5.1a8 8 0 0 1 4.3-3.6C8.8 5.5 8.3 6.7 8 8zm4 12c-.8-1.2-1.5-2.5-1.9-4h3.8c-.4 1.5-1.1 2.8-1.9 4zm2.3-6H9.7a14 14 0 0 1 0-4h4.6a14 14 0 0 1 0 4zm.3 5.6c.6-1.1 1.1-2.3 1.4-3.6h2.9a8 8 0 0 1-4.3 3.6zm1.8-5.6a16 16 0 0 0 0-4h3.3a8 8 0 0 1 0 4z"/></svg>
        <span>brightwirehollow.com.au</span>
      </div>
    </div>
    <div class="tagline-band">
      <svg viewBox="0 0 10 18"><polygon points="6,0 0,10 4,10 2,18 10,7 6,7 8,0"/></svg>
      <span class="tagline-band__hours">24/7</span>
      <span class="tagline-band__trade">Sydney Electrician</span>
    </div>
  </section>
</main>
</body>
</html>
```